TR Advisory Business Cards - High End AV / Low Voltage Company

We are low voltage AV company that specializes in high end clients on the residential side and larger businesses on the commercial side. We want something modern, tech looking but also something that is extremely professional looking. We have uploaded our logos and postcards we already have in the field. Along with a picture of one of our wrapped vans. Our website is at www.trvadvisory.example and our primary colors are the orange, green, grey and blue all military color finishes.

We are interesting in the slogans "Pairing You with the Right Technology" or "Connecting the Coast to Smart Tech"

Target Market(s)

We focus on 70% Commercial and 30% Residential Customers

Industry/Entity Type

Low Voltage, AV Company

Contact Information for Business Card

Name - Dorian Fairweather, Title - Owner, Office Phone - 555-714-3096, Mobile Phone - 555-802-4173, E-Mail - d@trvadvisory.example, Website: www.trvadvisory.example

Font styles to use
Sans Serif

Requirements
Must have
• Must have Name, Title, Work Phone & Mobile, Website and Logo.
Nice to have
• We want something that will impress our higher end clients with a great logo
Should not have
• Too traditional or plain.

```html
<!DOCTYPE html>
<html lang="en">
<head>
<meta charset="utf-8">
<title>TR Advisory Business Cards</title>
<link rel="stylesheet" href="https://fonts.googleapis.com/css2?family=Nunito:wght@400;600;700;800&display=swap">
<style>
  :root {
    --bg: #c4c4c4;
    --orange: #ee6a35;
    --orange-deep: #dd5c29;
    --orange-soft: #fbe3d8;
    --ink: #2b2b2b;
    --white: #ffffff;
  }
  * { margin: 0; padding: 0; box-sizing: border-box; }
  html, body {
    width: 1200px; height: 1200px; overflow: hidden;
    background: var(--bg);
    font-family: "Nunito", sans-serif;
  }
  .card {
    position: absolute;
    left: 170px;
    width: 861px;
    height: 503px;
  }
  .card-front { top: 76px; background: var(--white); }
  .card-back { top: 612px; height: 500px; background: var(--orange); }

  .holder-name {
    position: absolute; left: 71px; top: 166px;
    font-size: 30px; font-weight: 600; letter-spacing: 1px;
    color: var(--orange); text-transform: uppercase;
  }
  .holder-title {
    position: absolute; left: 71px; top: 208px;
    font-size: 21px; font-weight: 400; color: var(--ink);
  }
  .contact-list {
    position: absolute; left: 71px; top: 304px;
    list-style: none;
  }
  .contact-item {
    display: flex; align-items: center;
    height: 33.5px;
    font-size: 22px; color: var(--ink);
  }
  .contact-icon { width: 18px; height: 18px; margin-right: 16px; flex: none; }

  .brand-front {
    position: absolute; left: 560px; top: 115px; width: 270px;
    display: flex; align-items: center; justify-content: center; gap: 14px;
  }
  .brand-dot { width: 26px; height: 26px; border-radius: 50%; background: var(--orange); flex: none; }
  .brand-name {
    font-size: 40px; font-weight: 800; color: var(--orange); white-space: nowrap;
  }

  .corner-art {
    position: absolute; right: 0; bottom: 0;
    width: 356px; height: 204px;
    background: linear-gradient(135deg, rgba(251,227,216,0) 0%, var(--orange-soft) 55%, #f8cdb9 100%);
  }

  .brand-back {
    position: absolute; left: 0; right: 0; top: 205px;
    text-align: center;
    font-size: 72px; font-weight: 800; color: var(--orange-deep);
  }
  .slogan {
    position: absolute; left: 0; right: 0; top: 384px;
    text-align: center;
    font-size: 25px; font-weight: 400; color: var(--white);
  }
</style>
</head>
<body>
  <section class="card card-front">
    <div class="brand-front">
      <span class="brand-dot"></span>
      <span class="brand-name">TR Advisory</span>
    </div>

    <h1 class="holder-name">Dorian Fairweather</h1>
    <p class="holder-title">Owner</p>

    <ul class="contact-list">
      <li class="contact-item">
        <svg class="contact-icon" viewBox="0 0 24 24" aria-hidden="true"><path fill="#ee6a35" d="M6.6 10.8a15 15 0 0 0 6.6 6.6l2.2-2.2a1 1 0 0 1 1-.25 11.4 11.4 0 0 0 3.6.57 1 1 0 0 1 1 1V20a1 1 0 0 1-1 1A17 17 0 0 1 3 4a1 1 0 0 1 1-1h3.5a1 1 0 0 1 1 1c0 1.250.2 2.450.57 3.57a1 1 0 0 1-.25 1z"/></svg>
        555-714-3096
      </li>
      <li class="contact-item">
        <svg class="contact-icon" viewBox="0 0 24 24" aria-hidden="true"><rect x="6" y="2" width="12" height="20" rx="2" fill="none" stroke="#ee6a35" stroke-width="2"/><circle cx="12" cy="18" r="1.3" fill="#ee6a35"/></svg>
        555-802-4173
      </li>
      <li class="contact-item">
        <svg class="contact-icon" viewBox="0 0 24 24" aria-hidden="true"><rect x="2" y="5" width="20" height="14" rx="1.5" fill="#ee6a35"/><path d="M3 6l9 7 9-7" fill="none" stroke="#fff" stroke-width="1.6"/></svg>
        d@trvadvisory.example
      </li>
      <li class="contact-item">
        <svg class="contact-icon" viewBox="0 0 24 24" aria-hidden="true"><circle cx="12" cy="12" r="9.5" fill="none" stroke="#ee6a35" stroke-width="2"/><ellipse cx="12" cy="12" rx="4" ry="9.5" fill="none" stroke="#ee6a35" stroke-width="1.6"/><path d="M2.5 12h19M4 7h16M4 17h16" stroke="#ee6a35" stroke-width="1.4"/></svg>
        www.trvadvisory.example
      </li>
    </ul>

    <div class="corner-art" role="img" aria-label="Angular orange line-art pattern in the lower right corner"></div>
  </section>

  <section class="card card-back">
    <div class="brand-back">TR Advisory</div>
    <p class="slogan">Connecting the Coast to Smart Tech</p>
  </section>
</body>
</html>
```